MD Business Card

I want to create a simple business card.
I am a consultant. I design and develop furniture, lighting and accessories for hospitality and retail brands.
I want the card to be simple and clean. Not too much of a logo - but it needs the basic information shown on the attached file.
Also - I have shown some fonts that I like on the attached file.
The card can be square or rectangle. It should be double sided.
I prefer 1-2 colors (not too colorful - but using color an an accent) Even if using color on the edges as an accent.

My snapquilt link shows some other graphics styles that I like. I like clean and simple.
http://www.snapquilt.com/marendowsett/business-cards/

Reason: I needed a few more days to see some of the options evolve.

Hospitality

```html
<!DOCTYPE html>
<html lang="en">
<head>
<meta charset="utf-8">
<title>Maren Dowsett – Business Card</title>
<link rel="stylesheet" href="https://fonts.googleapis.com/css2?family=Didact+Gothic&family=Poiret+One&display=swap">
<style>
  :root {
    --backdrop: #b4b4b4;
    --card: #ffffff;
    --ink: #1a1a1a;
    --accent: #1aaea0;
  }
  html, body {
    margin: 0;
    padding: 0;
    width: 1200px;
    height: 612px;
    overflow: hidden;
    background: var(--backdrop);
    font-family: "Didact Gothic", "Century Gothic", sans-serif;
  }
  .canvas {
    position: relative;
    width: 1200px;
    height: 612px;
  }
  .card {
    position: absolute;
    top: 152px;
    width: 536px;
    height: 305px;
    background: var(--card);
    box-shadow: 0 1px 3px rgba(0,0,0,0.35);
  }
  .card--front { left: 37px; }
  .card--back  { left: 632px; }

  /* Front */
  .identity {
    position: absolute;
    left: 0;
    right: 0;
    top: 104px;
    text-align: center;
    color: var(--ink);
  }
  .identity__name {
    margin: 0;
    font-family: "Poiret One", "Century Gothic", sans-serif;
    font-weight: 400;
    font-size: 40px;
    line-height: 44px;
    letter-spacing: 0.5px;
    white-space: nowrap;
  }
  .identity__divider {
    width: 48px;
    height: 2px;
    margin: 10px auto 0;
    background: var(--accent);
  }
  .identity__tagline {
    margin: 12px 0 0 0;
    font-size: 16px;
    line-height: 20px;
    letter-spacing: 4px;
    text-transform: lowercase;
    white-space: nowrap;
  }

  /* Back */
  .contact {
    position: absolute;
    left: 0;
    right: 0;
    top: 127px;
    text-align: center;
  }
  .contact__email-row {
    display: flex;
    align-items: center;
    gap: 10px;
  }
  .contact__line {
    flex: 1;
    height: 1px;
    background: var(--accent);
  }
  .contact__email {
    font-size: 20px;
    line-height: 26px;
    color: var(--ink);
    white-space: nowrap;
  }
  .contact__phone {
    margin-top: 3px;
    font-size: 21px;
    line-height: 26px;
    letter-spacing: 1.5px;
    color: var(--accent);
  }
</style>
</head>
<body>
  <main class="canvas">
    <section class="card card--front" aria-label="Card front">
      <div class="identity">
        <h1 class="identity__name">MAREN DOWSETT</h1>
        <div class="identity__divider" aria-hidden="true"></div>
        <p class="identity__tagline">furniture · lighting · design</p>
      </div>
    </section>

    <section class="card card--back" aria-label="Card back">
      <div class="contact">
        <div class="contact__email-row">
          <span class="contact__line" aria-hidden="true"></span>
          <span class="contact__email">maren@marendowsett.com</span>
          <span class="contact__line" aria-hidden="true"></span>
        </div>
        <div class="contact__phone">917.555.0148</div>
      </div>
    </section>
  </main>
</body>
</html>
```